VERIDAX Need a luxury modern business card designed.

Need a luxury modern business card designed. refer to the uploaded files for the company name and logo in the zip file under source files. i will making my descion on monday. so please send in before then so if we need to edit we will have the time. we have a trade show coming up and im on a deadline for printer.

Target Market(s)

high end clients

Contact Information for Business Card

Company nAme and logo. Calvin Ostrow Co-Founder / Project Manager Office # 416-555-0193 Cell # 416-555-0147 VERIDAX.CA Calvin@veridax.ca

Font styles to use
Other font styles liked:
• Modern

Requirements
Must have
• Company name and logo, contact info, using the black, gold and white color scheme.

```html
<!DOCTYPE html>
<html lang="en">
<head>
<meta charset="utf-8">
<title>VERIDAX Business Card</title>
<link href="https://fonts.googleapis.com/css2?family=Lato:wght@300;400;700;900&display=swap" rel="stylesheet">
<style>
  :root {
    --backdrop: #2f2a27;
    --card-dark: #2b2b2b;
    --card-light: #ffffff;
    --gold: #a38f55;
    --ink: #2a2a2a;
    --white: #f4f2ee;
  }
  * { box-sizing: border-box; margin: 0; padding: 0; }
  html, body { width: 1200px; height: 847px; overflow: hidden; }
  body {
    background: var(--backdrop);
    font-family: 'Lato', sans-serif;
    position: relative;
  }
  .card {
    position: absolute;
    top: 275px;
    width: 520px;
    height: 297px;
    box-shadow: 0 10px 30px rgba(0,0,0,0.45);
  }
  .card--front { left: 55px; background: var(--card-dark); }
  .card--back { left: 625px; background: var(--card-light); }

  /* Front */
  .brand {
    position: absolute;
    left: 0; right: 0; top: 100px;
    text-align: center;
  }
  .brand__square {
    display: block;
    width: 18px; height: 18px;
    margin: 0 auto 16px;
    background: var(--gold);
  }
  .brand__name {
    color: var(--white);
    font-weight: 300;
    font-size: 44px;
    letter-spacing: 10px;
    padding-left: 10px;
    line-height: 1;
  }

  /* Back */
  .person {
    position: absolute;
    left: 16px; top: 98px;
    width: 200px;
    text-align: right;
  }
  .person__name {
    color: var(--gold);
    font-weight: 900;
    font-size: 21px;
    letter-spacing: -0.3px;
  }
  .person__title {
    color: var(--ink);
    font-size: 12.5px;
    margin-top: 3px;
  }
  .divider {
    position: absolute;
    left: 232px; top: 88px;
    width: 1px; height: 86px;
    background: var(--gold);
  }
  .contacts {
    position: absolute;
    left: 250px; top: 90px;
    list-style: none;
  }
  .contacts li {
    display: flex; align-items: center;
    color: var(--ink);
    font-size: 15px;
    height: 21px;
  }
  .contacts svg {
    width: 13px; height: 13px;
    margin-right: 12px;
    fill: none; stroke: var(--gold); stroke-width: 1.6;
  }
  .company-line {
    position: absolute;
    left: 62px; top: 212px;
    color: var(--gold);
    font-size: 13px;
    letter-spacing: 4.5px;
  }
</style>
</head>
<body>
  <section class="card card--front">
    <div class="brand">
      <span class="brand__square"></span>
      <div class="brand__name">VERIDAX</div>
    </div>
  </section>

  <section class="card card--back">
    <div class="person">
      <div class="person__name">Calvin Ostrow</div>
      <div class="person__title">Co-Founder / Project Manager</div>
    </div>
    <div class="divider"></div>
    <ul class="contacts">
      <li><svg viewBox="0 0 14 14"><path d="M2 5c0-2 10-2 10 0v1H9V5H5v1H2z"/><rect x="3" y="7" width="8" height="5"/></svg>416-555-0193</li>
      <li><svg viewBox="0 0 14 14"><rect x="4" y="1" width="6" height="12" rx="1"/></svg>416-555-0147</li>
      <li><svg viewBox="0 0 14 14"><rect x="1" y="3" width="12" height="8"/><path d="M1 3l6 5 6-5"/></svg>Calvin@veridax.ca</li>
      <li><svg viewBox="0 0 14 14"><circle cx="7" cy="7" r="5.5"/><path d="M1.5 7h11M7 1.5v11"/></svg>www.veridax.ca</li>
    </ul>
    <div class="company-line">VERIDAX LUXURY LANDSCAPES</div>
  </section>
</body>
</html>
```